physical therapy flyer

2 office locations speciality programs - work injury / Motor vehicle accidents - spanish speaking - do not put balance defecits/ fall prevention - Spanish speaking
neck and back pain shoulder pain/ rotator cuff disorder / bursitis
hip pain knee andle and foot pain post operative care including Spine , shoulder , knee , total joint replacement

Meadowlark Physical therapy & Chiropractic
4827 Ashbury BLvd
lindell park ny 11592
7185528174
3719 Tillman Parkway
Corvale NY 11592
7182947061
www.meadowlarkptchiroacu.com

```html
<!DOCTYPE html>
<html lang="es">
<head>
<meta charset="utf-8">
<title>Meadowlark Physical Therapy Flyer</title>
<link href="https://fonts.googleapis.com/css2?family=Poppins:wght@400;500;600;700&display=swap" rel="stylesheet">
<style>
  :root {
    --page-bg: #e9e9e9;
    --green-deep: #0b7d3e;
    --green-main: #4a9e3c;
    --green-bright: #7dbf3f;
    --green-ring: #3db54a;
    --mint: #eef6ea;
    --ink: #4a4a4a;
    --charcoal: #323233;
    --white: #ffffff;
  }
  * { margin: 0; padding: 0; box-sizing: border-box; }
  html, body { width: 1200px; height: 1200px; overflow: hidden; }
  body {
    background: var(--page-bg);
    font-family: "Poppins", sans-serif;
    position: relative;
  }
  .flyer {
    position: absolute;
    left: 151px; top: 20px;
    width: 897px; height: 1160px;
    overflow: hidden;
    background: linear-gradient(180deg, #ffffff 40%, var(--mint) 80%);
    box-shadow: 0 2px 10px rgba(0,0,0,0.15);
  }
  .backdrop { position: absolute; inset: 0; }
  .hero-photo {
    position: absolute;
    left: 470px; top: 0;
    width: 427px; height: 470px;
    background: linear-gradient(90deg, rgba(74,158,60,0) 0%, rgba(60,140,60,0.65) 35%, rgba(40,110,55,0.85) 100%);
  }
  .brand-mark {
    position: absolute;
    left: 50px; top: 74px;
    display: flex; align-items: center; gap: 12px;
    color: var(--white);
    font-size: 19px; font-weight: 400; line-height: 23px;
  }
  .brand-mark .dot {
    width: 34px; height: 34px; border-radius: 50%;
    border: 2px solid var(--white);
    flex: none;
  }
  .headline {
    position: absolute;
    left: 53px; top: 148px;
    color: var(--white);
    font-size: 44px; font-weight: 700; line-height: 53px;
    letter-spacing: -0.3px;
  }
  .subline {
    position: absolute;
    left: 53px; top: 318px;
    color: var(--white);
    font-size: 26px; font-weight: 400; line-height: 32px;
  }
  .condition {
    position: absolute;
    width: 180px;
    text-align: center;
    color: var(--ink);
    font-size: 16px; font-weight: 500; line-height: 20px;
  }
  .condition .badge {
    position: absolute;
    left: 50%; transform: translateX(-50%);
    width: 140px; height: 140px; border-radius: 50%;
    background: rgba(61,181,74,0.35);
    display: flex; align-items: center; justify-content: center;
  }
  .condition .badge span {
    width: 126px; height: 126px; border-radius: 50%;
    background: var(--green-deep);
  }
  .condition .label { position: absolute; left: 0; width: 180px; }
  .care-heading {
    position: absolute;
    left: 0; top: 670px; width: 897px;
    text-align: center;
    font-size: 32px; font-weight: 700; line-height: 40px;
    color: var(--green-deep);
  }
  .care-heading .light { color: var(--green-main); }
  .care-photo {
    position: absolute;
    top: 771px; width: 191px; height: 131px;
    border-radius: 8px;
  }
  .care-label {
    position: absolute;
    top: 910px;
    text-align: center;
    color: var(--ink);
    font-size: 17px; font-weight: 700; line-height: 22px;
  }
  .footer-brand {
    position: absolute;
    left: 55px; top: 1050px;
    color: var(--white);
    font-size: 20px; font-weight: 700; line-height: 25px;
  }
  .footer-brand .web {
    display: block; margin-top: 4px;
    font-size: 15px; font-weight: 400;
  }
  .office {
    position: absolute;
    top: 1052px;
    color: var(--white);
    font-size: 16.5px; font-weight: 400; line-height: 21px;
  }
  .office .line { display: flex; gap: 8px; align-items: flex-start; }
  .office svg { flex: none; margin-top: 2px; }
  .office .phone { margin-top: 9px; font-size: 18.5px; font-weight: 700; align-items: center; }
  .divider {
    position: absolute;
    left: 599px; top: 1058px;
    width: 1px; height: 78px;
    background: rgba(255,255,255,0.6);
  }
</style>
</head>
<body>
<main class="flyer">
  <svg class="backdrop" viewBox="0 0 897 1160" width="897" height="1160" aria-hidden="true">
    <defs>
      <linearGradient id="heroGreen" x1="0" y1="0" x2="1" y2="1">
        <stop offset="0" stop-color="#5aa842"/>
        <stop offset="1" stop-color="#2f8a45"/>
      </linearGradient>
    </defs>
    <path d="M0 0 H897 V441 Q448 600 0 445 Z" fill="url(#heroGreen)"/>
    <path d="M0 445 Q448 600 897 441" fill="none" stroke="#1f7a3a" stroke-width="6"/>
    <path d="M0 452 Q448 612 897 448" fill="none" stroke="#3db54a" stroke-width="5"/>
    <path d="M0 990 C300 1010 620 935 897 972 V1160 H0 Z" fill="var(--charcoal)"/>
    <path d="M0 942 Q160 1012 540 998 Q180 1035 0 985 Z" fill="#3f9c3a"/>
    <path d="M0 955 Q170 1008 460 1002 Q170 1022 0 982 Z" fill="#1f8a3a"/>
    <path d="M600 966 Q770 944 897 980 V1000 Q770 962 600 966 Z" fill="#3f9c3a"/>
  </svg>

  <div class="hero-photo" role="img" aria-label="Photo of a therapist holding a spine model while talking with a patient"></div>

  <div class="brand-mark">
    <span class="dot"></span>
    <span>Meadowlark Physical Therapy,<br>Chiropractic, and Acupuncture</span>
  </div>

  <h1 class="headline">Lesiones laborales<br>/ Accidentes<br>automovilísticos</h1>
  <p class="subline">No ponga déficit de<br>equilibrio/prevención<br>de caídas</p>

  <div class="condition" style="left:90px; top:437px;">
    <div class="badge" role="img" aria-label="Icon of a person with neck and back pain"><span></span></div>
    <div class="label" style="top:151px;">Neck and Back<br>pain</div>
  </div>
  <div class="condition" style="left:275px; top:455px;">
    <div class="badge" role="img" aria-label="Icon of a person with shoulder pain"><span></span></div>
    <div class="label" style="top:151px;">Shoulder pain</div>
  </div>
  <div class="condition" style="left:457px; top:455px;">
    <div class="badge" role="img" aria-label="Icon of a shoulder joint with rotator cuff"><span></span></div>
    <div class="label" style="top:151px;">Rotator Cuff<br>disorder</div>
  </div>
  <div class="condition" style="left:639px; top:437px;">
    <div class="badge" role="img" aria-label="Icon of a knee joint"><span></span></div>
    <div class="label" style="top:151px;">Bursitis</div>
  </div>

  <h2 class="care-heading">Hip pain knee handle <span class="light">and foot pain post</span><br>operative care <span class="light">including</span></h2>

  <div class="care-photo" style="left:54px; background:linear-gradient(135deg,#c9d3da,#4f6a7e 60%,#8fa2ad);" role="img" aria-label="Photo of a therapist supporting an older man's lower back"></div>
  <div class="care-photo" style="left:255px; background:linear-gradient(135deg,#f2f0ee,#dcc9bd 50%,#9ed27a);" role="img" aria-label="Photo of a therapist raising a woman's arm to test the shoulder"></div>
  <div class="care-photo" style="left:455px; background:linear-gradient(135deg,#6d7a6a,#2d3a35 50%,#c89a84);" role="img" aria-label="Photo of a tennis player holding her injured knee on court"></div>
  <div class="care-photo" style="left:657px; background:linear-gradient(135deg,#eeeae6,#e3c4ae 50%,#2c3c5a);" role="img" aria-label="Photo of a therapist stretching a patient's leg after joint replacement"></div>

  <div class="care-label" style="left:54px; width:191px;">Spine</div>
  <div class="care-label" style="left:255px; width:191px;">Shoulder</div>
  <div class="care-label" style="left:455px; width:191px;">Knee</div>
  <div class="care-label" style="left:657px; width:191px;">Total joint<br>replacement</div>

  <div class="footer-brand">Meadowlark Physical<br>therapy &amp; Chiropractic<span class="web">www.meadowlarkptchiroacu.com</span></div>

  <div class="office" style="left:365px;">
    <div class="line">
      <svg width="14" height="19" viewBox="0 0 14 19" aria-hidden="true"><path d="M7 1a6 6 0 0 0-6 6c0 4.5 6 11 6 11s6-6.5 6-11a6 6 0 0 0-6-6z" fill="none" stroke="#fff" stroke-width="2"/><circle cx="7" cy="7" r="2.2" fill="#fff"/></svg>
      <span>4827 Ashbury BLvd<br>lindell park ny 11592</span>
    </div>
    <div class="line phone">
      <svg width="14" height="16" viewBox="0 0 14 16" aria-hidden="true"><path d="M3 1l3 3-2 2c1 2 3 4 5 5l2-2 3 3-2 3C6 14 0 8 1 3z" fill="none" stroke="#fff" stroke-width="1.8" stroke-linejoin="round"/></svg>
      <span>7185528174</span>
    </div>
  </div>

  <div class="divider"></div>

  <div class="office" style="left:629px;">
    <div class="line">
      <svg width="14" height="19" viewBox="0 0 14 19" aria-hidden="true"><path d="M7 1a6 6 0 0 0-6 6c0 4.5 6 11 6 11s6-6.5 6-11a6 6 0 0 0-6-6z" fill="none" stroke="#fff" stroke-width="2"/><circle cx="7" cy="7" r="2.2" fill="#fff"/></svg>
      <span>3719 Tillman Parkway<br>Corvale NY 11592</span>
    </div>
    <div class="line phone">
      <svg width="14" height="16" viewBox="0 0 14 16" aria-hidden="true"><path d="M3 1l3 3-2 2c1 2 3 4 5 5l2-2 3 3-2 3C6 14 0 8 1 3z" fill="none" stroke="#fff" stroke-width="1.8" stroke-linejoin="round"/></svg>
      <span>7182947061</span>
    </div>
  </div>
</main>
</body>
</html>
```